Auction Company Wordpress Design Project

We need a WordPress design/concept for an established auctioneering company specializing in Benefit Auctions, Estate Auctions, Business Liquidations/Overstocks, and real estate marketing in the Chicago area. The winning design will have a professional look appealing to clients searching for these services.

Industry/Entity Type

Real Estate

Requirements
Must have
• - We will require winning designer to provide a layered PSD (Adobe photoshop) concept file, along with any non-standard font files used.

The site's navigation: 1) Home, 2) Auctions, 3) About Us, 4) Buyers, 5) Sellers, 6) Media, 7) Contact Us. Horizontal structure preferred.

A slideshow element will be represented (choice of files attached) preferably in the header. The following widgets will also be incorporated into sidebar (or other creative placement):
- Brightway Mailer email signup
- Featured Auctions (example shown in http://www.bidlantern-example.com/ as "Upcoming Auctions" widget)
- Vidora video widget
- Social media widget for Friendlyn, Chirpel, Vidora icons
- Testimonials widget

Winning design will creatively use colors in logo (with perhaps accent color) with a professional, clean look. Client mentions liking the use of color in http://www.plotgleam-example.com/

Footer of site will have generic contact info (phone number, email addresses, mailing address; a smaller instance of logo; and the attached association logos.
Nice to have
• - Use of drop-down menus should be demonstrated by incorporating mouse-over for 1) Upcoming, 2) Online, 3) Past, under the 'Auctions' main menu item (for clarity of design, this drop-down can be placed under any other menu item if necessary).
Should not have
• Please do not use auction gavels in the design.

```html
<!DOCTYPE html>
<html lang="en">
<head>
<meta charset="utf-8">
<title>Lakeshore Auctioneering &amp; Realty</title>
<link rel="stylesheet" href="https://fonts.googleapis.com/css2?family=Arimo:wght@400;700&family=Arvo:wght@400;700&family=Gelasio:ital,wght@0,400;0,700;1,400&family=Libre+Baskerville:wght@400;700&family=Source+Sans+3:wght@400;600&display=swap">
<style>
:root{
  --header-dark:#123432;
  --header-mid:#1d4a47;
  --band-teal:#2b7772;
  --band-deep:#1f5c58;
  --cream:#fdf9ec;
  --title-cream:#f3ecd2;
  --nav-teal:#9fd9d4;
  --teal-text:#226f6a;
  --body-text:#3d3a36;
  --rule:#bdb6a6;
  --magenta:#a3224f;
  --details-blue:#5ccbee;
  --details-text:#155b86;
  --drop-beige:#ebe3d0;
  --white:#ffffff;
}
*{margin:0;padding:0;box-sizing:border-box}
html,body{width:873px;height:1200px;overflow:hidden;background:var(--cream)}
.page{position:absolute;left:0;top:0;width:800px;height:1100px;transform:scale(1.09125,1.0909);transform-origin:0 0;background:var(--cream);font-family:"Gelasio",Georgia,serif;color:var(--body-text)}
.abs{position:absolute}

/* header */
.header{left:0;top:0;width:800px;height:106px;background:radial-gradient(ellipse at 50% 0%,#2c5f5b 0%,var(--header-mid) 40%,var(--header-dark) 100%)}
.logo-box{left:142px;top:28px;width:76px;height:76px;background:var(--white);display:flex;align-items:center;justify-content:center;text-align:center;font-family:"Libre Baskerville",serif;font-size:9px;line-height:1.15;color:#3a3a3a;padding:4px}
.site-title{left:245px;top:40px;font-family:"Libre Baskerville",serif;font-weight:700;font-size:19px;letter-spacing:0;color:var(--title-cream)}
.nav{left:257px;top:87px;display:flex;font-family:"Source Sans 3",sans-serif;font-size:12px;color:var(--nav-teal)}
.nav span{margin-right:20px}
.nav .active{color:var(--white)}
.band{left:0;top:106px;width:800px;height:210px;background:linear-gradient(180deg,var(--band-deep) 0%,var(--band-teal) 30%,var(--band-teal) 80%,#2f807a 100%)}
.band-shadow{left:0;top:316px;width:800px;height:45px;background:linear-gradient(180deg,rgba(0,0,0,.08),rgba(0,0,0,0))}

/* dropdown */
.dropdown{left:305px;top:110px;width:111px;height:78px;background:var(--drop-beige);box-shadow:0 2px 4px rgba(0,0,0,.35);font-family:"Gelasio",serif;font-style:italic;font-size:9.5px;color:#4a463c;padding:13px 0 0 13px;line-height:23px;z-index:2}

/* hero */
.hero-frame{left:73px;top:118px;width:395px;height:230px;background:var(--white);border-radius:3px;box-shadow:0 2px 6px rgba(0,0,0,.3)}
.hero-photo{left:77px;top:122px;width:387px;height:222px;background:linear-gradient(180deg,#4f7fc4 0%,#8aa6cf 40%,#d9cfbf 60%,#6c6a62 100%)}

/* featured auction */
.feature{left:485px;top:118px;width:244px;height:228px;background:linear-gradient(180deg,#f4f4f4,#e4e4e4);border-radius:3px;box-shadow:0 2px 6px rgba(0,0,0,.3);text-align:center}
.feature-title{position:absolute;top:11px;width:100%;font-family:"Libre Baskerville",serif;font-size:12.5px;letter-spacing:.5px;color:#333}
.feature-meta{position:absolute;top:34px;width:100%;font-family:"Gelasio",serif;font-size:10px;line-height:13.5px;color:var(--magenta)}
.feature-meta b{font-weight:700}
.feature-rule{position:absolute;left:0;top:79px;width:100%;height:1px;background:#c9c9c9}
.feature-photo{position:absolute;left:14px;top:91px;width:96px;height:94px;background:linear-gradient(160deg,#3a3633,#7a6e60 50%,#2b2826)}
.feature-list{position:absolute;left:118px;top:92px;width:112px;text-align:left;list-style:none;font-family:"Arimo",sans-serif;font-weight:700;font-size:7.8px;line-height:10.5px;color:#3a3a3a}
.feature-list li{padding-left:6px;text-indent:-6px;margin-bottom:2.5px}
.details-btn{position:absolute;left:130px;top:193px;width:77px;height:21px;background:linear-gradient(180deg,#8fdcf6,var(--details-blue));border:1px solid #3fa9cf;font-family:"Libre Baskerville",serif;font-weight:700;font-size:11px;line-height:19px;color:var(--details-text)}

/* main column */
.main{left:78px;top:369px;width:429px}
.main h2{font-family:"Arvo",serif;font-weight:700;font-size:12px;color:#3a3632}
.rule{height:0;border-top:1px solid var(--rule);border-bottom:1px solid #fff}
.intro-quote{font-family:"Gelasio",serif;font-weight:700;font-size:9.4px;line-height:15.5px;color:var(--teal-text);padding:3px 0 5px}
.copy{font-size:8.9px;line-height:11.6px;text-align:left}
.service{padding:9px 0 9px;font-size:8.9px;line-height:11.6px}
.service b{font-weight:700;color:var(--teal-text)}
.more{font-family:"Gelasio",serif;font-weight:700;font-size:9.5px;color:var(--teal-text);letter-spacing:.3px}

/* sidebar */
.newsletter{left:530px;top:383px;width:199px;height:113px;background:var(--white);box-shadow:0 1px 4px rgba(0,0,0,.18);padding:12px 16px}
.newsletter h3{font-family:"Arimo",sans-serif;font-weight:400;font-size:12.5px;color:#222;padding-bottom:8px;border-bottom:1px solid #ccc}
.newsletter p{font-family:"Arimo",sans-serif;font-size:6.8px;line-height:9.5px;color:#555;margin-top:9px}
.news-input{position:absolute;left:17px;top:75px;width:167px;height:19px;background:#2b2b2b;border-radius:4px;font-family:"Arimo",sans-serif;font-size:6.8px;color:#ddd;line-height:19px;padding-left:6px}
.news-btn{position:absolute;right:2px;top:2px;width:44px;height:15px;background:linear-gradient(#f6f6f6,#d6d6d6);border-radius:3px;color:#222;line-height:15px;text-align:center}
.video{left:531px;top:513px;width:197px;height:140px;background:radial-gradient(ellipse at 45% 40%,#3b63b8 0%,#1c357a 60%,#0e1d47 100%);border:2px solid #cfd6e4}
.video-bar{position:absolute;left:0;bottom:0;width:100%;height:10px;background:#1a2233}
.video-bar i{position:absolute;left:28px;top:4px;width:120px;height:2px;background:#7a8aa8}
.side-divider{left:518px;top:666px;width:2px;height:303px;background:#8c8c8c}
.side-rule{height:0;border-top:1px solid var(--rule)}
.find-us{left:530px;top:666px;width:199px}
.find-us h4{text-align:center;font-family:"Arvo",serif;font-weight:700;font-size:10.5px;letter-spacing:.5px;color:#333;margin-top:12px}
.socials{display:flex;justify-content:space-between;padding:5px 22px 0 22px;height:76px}
.social{width:44px;height:44px;border:1px solid #b8b1a0;display:flex;align-items:center;justify-content:center;font-family:"Gelasio",serif;font-size:7.5px;color:var(--teal-text)}
.testimonials{left:537px;top:753px;width:192px;font-size:8.9px;line-height:11.6px}
.testimonials h4{font-family:"Arvo",serif;font-weight:700;font-size:11px;color:#333;margin:8px 0 4px}
.testimonials p{margin-bottom:4px}
.testimonials b{color:var(--teal-text)}

/* footer */
.footer{left:0;top:978px;width:800px;height:84px;background:linear-gradient(180deg,#163e3b 0%,var(--band-teal) 20%,var(--band-teal) 75%,#1d524e 100%)}
.footer-logo{position:absolute;left:78px;top:22px;width:40px;height:40px;background:var(--white);font-family:"Libre Baskerville",serif;font-size:5px;line-height:1.2;color:#333;display:flex;align-items:center;justify-content:center;text-align:center;padding:2px}
.contact{position:absolute;left:127px;top:21px;font-size:9px;line-height:15.5px;color:var(--white)}
.badges{position:absolute;left:588px;top:26px;display:flex;gap:14px}
.badge{width:32px;height:38px;background:#14312f;border-radius:3px}
.copyright{left:0;top:1076px;width:800px;text-align:center;font-family:"Gelasio",serif;font-weight:700;font-size:7.5px;color:var(--teal-text)}
</style>
</head>
<body>
<div class="page">
  <header class="abs header"></header>
  <div class="abs logo-box">Lakeshore Auctioneering &amp; Realty</div>
  <div class="abs site-title">LAKESHORE AUCTIONEERING &amp; REALTY</div>
  <nav class="abs nav">
    <span>Home</span><span class="active">Auctions</span><span>About Us</span><span>Buyers</span><span>Sellers</span><span>Media</span><span>Contact Us</span>
  </nav>
  <div class="abs band"></div>
  <div class="abs band-shadow"></div>

  <div class="abs hero-frame"></div>
  <div class="abs hero-photo" role="img" aria-label="Slideshow photo of a two-storey suburban house at dusk with an auction sign on the lawn"></div>

  <div class="abs dropdown">Upcoming<br>Online<br>Past</div>

  <section class="abs feature">
    <div class="feature-title">CBD APARTMENT AUCTION</div>
    <div class="feature-meta">Original Price: $6.1M<br>Sealed Bid Auction, Jan. 7th<br><b>Published Reserve $3.8 M</b></div>
    <div class="feature-rule"></div>
    <div class="feature-photo" role="img" aria-label="Photo of a modern apartment kitchen interior"></div>
    <ul class="feature-list">
      <li>- 4,200 sq.ft.</li>
      <li>- Open floor plans</li>
      <li>- 4 bdrms</li>
      <li>- 4.5 baths</li>
      <li>- Additional 1,642 sq.ft. in decks, balconies, &amp; garden loggia</li>
      <li>- Elevator</li>
    </ul>
    <div class="details-btn">DETAILS</div>
  </section>

  <main class="abs main">
    <h2>Welcome to Lakeshore Auctioneering &amp; Realty</h2>
    <div class="rule" style="margin-top:2px"></div>
    <p class="intro-quote">"Neque porro quisquam est qui dolorem ipsum quia dolor sit amet, consectetur, adipisci velit...Suspendisse venenatis dolor id massa condimentum id blandit diam placerat. Nam rhoncus nibh nec enim gravida at blandit sem auctor."</p>
    <div class="rule"></div>
    <p class="copy" style="margin-top:8px">Lorem ipsum dolor sit amet, consectetur adipiscing elit. Aliquam suscipit, mi non blandit interdum, nisi dui commodo purus, ut eleifend lorem eros eget velit. Aliquam erat volutpat. Phasellus molestie posuere tortor eu blandit. Nulla iaculis, velit id tempus lacinia, risus mi consequat nisi, et pulvinar sem est ut felis. Aliquam nulla magna, blandit at egestas et, euismod eleifend nisi. Nunc lacus nulla, iaculis a elementum eget, tincidunt eget ipsum. Mauris turpis magna, gravida viverra pellentesque quis, viverra vitae diam. Curabitur hendrerit convallis interdum. Nunc a mauris augue. Vivamus molestie aliquam augue, ut venenatis augue placerat nec. Cras volutpat tincidunt tellus. Fusce congue commodo urna.</p>
    <p class="copy" style="margin-top:14px">Mauris nec mattis odio. Donec in orci orci. Nam diam neque, imperdiet ac porttitor et, auctor ut lacus. Maecenas molestie lorem at metus aliquam placerat. Lorem ipsum dolor sit amet, consectetur adipiscing elit. Aliquam euismod vestibulum nunc eu scelerisque. Aenean dapibus elit vitae elit sollicitudin scelerisque. Integer commodo fringilla sapien in pharetra.</p>
    <div class="rule" style="margin-top:7px"></div>
    <h2 style="margin:10px 0 6px">We Specializing in:</h2>
    <div class="rule"></div>
    <p class="service" style="padding-top:11px"><b>Benefit Auctions</b>:&nbsp; Neque porro quisquam est qui dolorem ipsum quia dolor sit amet, consectetur, adipisci velit...Suspendisse venenatis dolor id massa condimentum id blandit diam placerat. Nam rhoncus nibh nec enim gravida at blandit sem auctor."</p>
    <div class="rule"></div>
    <p class="service"><b>Estate Auctions</b>:&nbsp; Neque porro quisquam est qui dolorem ipsum quia dolor sit amet, consectetur, adipisci velit...Suspendisse venenatis dolor id massa condimentum id blandit diam placerat. Nam rhoncus nibh nec enim gravida at blandit sem auctor."</p>
    <div class="rule"></div>
    <p class="service"><b>Business Liquidations/Overstocks</b>:&nbsp; Neque porro quisquam est qui dolorem ipsum quia dolor sit amet, consectetur, adipisci velit...Suspendisse venenatis dolor id massa condimentum id blandit diam placerat. Nam rhoncus nibh nec enim gravida at blandit sem auctor."</p>
    <div class="rule"></div>
    <p class="service"><b>real estate marketing</b>:&nbsp; Neque porro quisquam est qui dolorem ipsum quia dolor sit amet, consectetur, adipisci velit...Suspendisse venenatis dolor id massa condimentum id blandit diam placerat. Nam rhoncus nibh nec enim gravida at blandit sem auctor."</p>
    <div class="rule"></div>
    <p class="more" style="margin-top:4px;margin-left:-2px">Find Out More....</p>
  </main>

  <aside>
    <section class="abs newsletter">
      <h3>Subscribe to newsletter</h3>
      <p>Sign up with your email to get updates about new resources releases and special offers.</p>
      <div class="news-input">enter your email here<span class="news-btn">subscribe</span></div>
    </section>

    <div class="abs video" role="img" aria-label="Video player showing a promotional clip with a play button">
      <svg class="abs" style="left:70px;top:38px" width="54" height="54" viewBox="0 0 54 54"><circle cx="27" cy="27" r="25" fill="rgba(255,255,255,.25)" stroke="#fff" stroke-width="2"/><path d="M20 14 L40 27 L20 40 Z" fill="#fff"/></svg>
      <div class="video-bar"><i></i></div>
    </div>

    <div class="abs side-divider"></div>

    <section class="abs find-us">
      <div class="side-rule"></div>
      <h4>FIND US ON:</h4>
      <div class="socials">
        <div class="social">Friendlyn</div>
        <div class="social">Chirpel</div>
        <div class="social">Vidora</div>
      </div>
    </section>

    <section class="abs testimonials">
      <div class="side-rule" style="margin-left:-7px"></div>
      <h4>What do our customers say:</h4>
      <p><b>Peter</b>:&nbsp; "Neque porro quisquam est qui dolorem ipsum quia dolor sit amet, consectetur, adipisci velit...Suspendisse venenatis dolor id massa condimentum id blandit diam placerat. Nam rhoncus nibh nec enim gravida at blandit sem auctor."</p>
      <p><b>Rachel</b>:&nbsp; "Neque porro quisquam est qui dolorem ipsum quia dolor sit amet, consectetur, adipisci velit...Suspendisse venenatis dolor id massa."</p>
      <p><b>Jared</b>:&nbsp; "Neque porro quisquam est qui dolorem ipsum quia dolor sit amet, consectetur, adipisci velit...Suspendisse venenatis dolor id."</p>
      <p class="more" style="text-align:right;margin-top:6px;margin-right:14px">Find Out More....</p>
    </section>
  </aside>

  <footer class="abs footer">
    <div class="footer-logo">Lakeshore Auctioneering &amp; Realty</div>
    <div class="contact">Phone Number: 011-2468 1357<br>Email Addresses: sampleemail@mailnest-example.com<br>Mailing Address: 48 Harbor Lane, Elmstead, 6061</div>
    <div class="badges"><div class="badge"></div><div class="badge"></div><div class="badge"></div></div>
  </footer>
  <p class="abs copyright">Copyright © 2012 Lakeshore Auctioneering &amp; Realty. All rights reserved.</p>
</div>
</body>
</html>
```